Bref créative
Brochure for a Peforming Arts Private School
Whitford Lane
Institute of Global Learning, Creative and Stage Crafts
Vision:
Whitford Lane Academy will engage and enrich students using the fine arts and a rigorous curriculum so that they are prepared for life after school. Through the fine arts, students become more successful and experience the world in a more holistic manner. Through rigorous curriculum, students are prepared for professional opportunities. Students will focus their passion for music, theater, art, dance, and international studies.
I will upload the school's prospectus to provide other details that might be important to add.
Education
The target audience is more for Corporate and Parent meetings, so that the company can introduce itself and the audience can have something to take with them.
I would like the brochure to have the following:
1. Color
2. Professional Look
3. School Logo
4. Information about the school - including vision, majors, course types, etc.
4. Non-discrimanatory policy - written in smaller print at the bottom of the back of the brochure
5. Visuals to represent the ideas of theater, dance, art, music, and international studies.
Please use the first paragraph.

```html
<!DOCTYPE html>
<html lang="en">
<head>
<meta charset="utf-8">
<title>Whitford Lane Academy Brochure</title>
<link href="https://fonts.googleapis.com/css2?family=Cinzel:wght@600&family=Lato:wght@400;700&family=Playfair+Display:ital@1&display=swap" rel="stylesheet">
<style>
:root{
  --bg:#e9e4dc;
  --paper:#ffffff;
  --cream:#efe6d6;
  --navy:#26283f;
  --purple:#4a3a6b;
  --gold:#c9a24a;
  --red:#a4161a;
  --ink:#3b3b3b;
  --muted:#7a7a7a;
  --rowgray:#a9a9a9;
}
*{box-sizing:border-box;margin:0;padding:0}
html,body{width:1200px;height:515px;overflow:hidden}
body{background:var(--bg);font-family:'Lato',sans-serif;color:var(--ink);position:relative}
.brochure{position:absolute;display:flex;box-shadow:0 4px 14px rgba(0,0,0,.25)}
.outside{left:20px;top:32px;width:530px;height:450px}
.inside{left:575px;top:22px;width:605px;height:470px;flex-direction:column;background:var(--paper)}
.panel{flex:1 1 0;min-width:0;padding:16px 14px;position:relative;overflow:hidden}
.panel p{font-size:6.5px;line-height:1.45;margin-bottom:7px}
.panel h3{font-size:7.5px;font-weight:700;margin-bottom:4px}
.info{background:var(--paper)}
.schedule{width:100%;border-collapse:collapse;margin:6px 0 10px;font-size:6px}
.schedule th{background:var(--navy);color:#fff;padding:4px;font-weight:700}
.schedule td{background:var(--rowgray);color:#fff;padding:4px;border-bottom:2px solid #fff}
.stage{background:var(--cream);display:flex;flex-direction:column;align-items:center;padding:22px 0 18px}
.stage-art{width:100%;flex:1;margin:14px 0 16px;background:linear-gradient(180deg,#8e1417 0%,#b8262b 55%,#d9b765 100%)}
.contact{text-align:center;font-size:6px;line-height:1.6;color:var(--muted)}
.cover{background:var(--navy);color:#fff;display:flex;flex-direction:column;align-items:center;text-align:center;padding-top:40px}
.cover-title{font-family:'Cinzel',serif;font-size:17px;line-height:1.25;color:var(--gold);white-space:nowrap}
.rule{width:80%;height:1px;background:var(--gold);margin:12px 0 28px}
.mark{display:flex;align-items:center;gap:5px;font-family:'Cinzel',serif;color:var(--gold);font-size:9px;white-space:nowrap}
.mark i{width:10px;height:10px;border-radius:50%;background:var(--gold);display:block;flex:none}
.tagline{font-family:'Playfair Display',serif;font-style:italic;font-size:12.5px;line-height:1.35;margin-top:auto;margin-bottom:40px;padding:0 10px}
.topbar{height:14px;background:linear-gradient(90deg,var(--navy) 0 60%,var(--purple) 60% 85%,var(--gold) 85%)}
.spread{display:flex;flex:1}
.buttons{display:flex;gap:5px;margin:6px 0 10px}
.buttons span{font-size:6px;color:#fff;padding:4px 8px;background:var(--navy)}
.buttons span:nth-child(2){background:var(--gold)}
.buttons span:nth-child(3){background:var(--purple)}
.plain{width:100%;border-collapse:collapse;font-size:5.5px}
.plain td{border:1px solid #ccc;padding:2px 4px}
.photo{width:100%;height:90px;display:block;margin-bottom:6px;background:#7d6a8c}
.photos{padding:10px;display:flex;flex-direction:column;gap:6px}
.photos div{flex:1}
.head-mark{justify-content:center;margin:6px 0 10px;color:var(--navy)}
.head-mark i{background:var(--navy)}
</style>
</head>
<body>
<section class="brochure outside">
  <div class="panel info">
    <h3>Schedule</h3>
    <p>Whitford Lane Academy offers flexible daily blocks so students balance studio time with core academics and global studies each week.</p>
    <table class="schedule">
      <tr><th>Block</th><th>Course</th></tr>
      <tr><td>Block 1 8:00</td><td>Core Studies</td></tr>
      <tr><td>Block 2 9:30</td><td>Language</td></tr>
      <tr><td>Block 3 11:00</td><td>Music</td></tr>
      <tr><td>Block 4 12:30</td><td>Theater</td></tr>
      <tr><td>Block 5 2:00</td><td>Visual Art</td></tr>
      <tr><td>Block 6 3:30</td><td>Dance</td></tr>
    </table>
    <p>Students rotate through ensemble rehearsals and electives, with advisors guiding each plan toward university and career goals.</p>
    <h3>Nondiscriminatory Policy</h3>
    <p>Whitford Lane Academy admits students of any race, color, religion, or national origin to all rights and programs, and does not discriminate in admissions, aid or activities.</p>
  </div>
  <div class="panel stage">
    <div class="mark head-mark"><i></i>Whitford Lane Academy</div>
    <div class="stage-art" role="img" aria-label="Illustration of red stage curtains with gold theater masks"></div>
    <div class="contact">1400 Harlow Square, Ashfield<br>Phone: (555) 014-2290<br>Fax: (555) 014-2291</div>
  </div>
  <div class="panel cover">
    <div class="cover-title">Whitford Lane<br>Academy</div>
    <div class="rule"></div>
    <div class="mark"><i></i>Whitford Lane Academy</div>
    <div class="tagline">Passion for music,<br>Theater, Art, Dance,<br>and International Studies</div>
  </div>
</section>

<section class="brochure inside">
  <div class="topbar"></div>
  <div class="spread">
    <div class="panel">
      <div class="mark head-mark"><i></i>Whitford Lane Academy</div>
      <h3>Vision</h3>
      <p>Whitford Lane Academy will engage and enrich students using the fine arts and a rigorous curriculum so that they are prepared for life after school. Through the fine arts, students become more successful and experience the world in a more holistic manner. Through rigorous curriculum, students are prepared for professional opportunities. Students will focus their passion for music, theater, art, dance, and international studies.</p>
      <div class="buttons"><span>Inquire</span><span>Enroll</span><span>Explore</span></div>
      <h3>Majors</h3>
      <p>Students select one major and explore others through electives, gaining depth and range across creative disciplines.</p>
      <table class="plain">
        <tr><td>Music</td><td>Theater</td><td>Visual Art</td></tr>
        <tr><td>Dance</td><td>Languages</td><td>Global Studies</td></tr>
      </table>
    </div>
    <div class="panel">
      <h3>Course Types</h3>
      <p>Our program blends honors academics with studio practice. Students complete core classes in math, science and writing alongside daily arts training.</p>
      <div class="photo" role="img" aria-label="Photo of students performing in a theater class"></div>
      <p>Advanced courses prepare students for auditions, portfolios and exchange programs abroad, building confidence and a global outlook.</p>
      <p>Faculty include working artists and scholars who mentor each student through showcases, recitals and exhibitions every term.</p>
      <p>Families are welcome at open rehearsals and seasonal performances throughout the school year.</p>
    </div>
    <div class="panel photos">
      <div role="img" aria-label="Photo of smiling students with books" style="background:linear-gradient(#c9b9a0,#8d7a66)"></div>
      <div role="img" aria-label="Photo of sheet music and instruments" style="background:linear-gradient(#d8d2c6,#9a948a)"></div>
      <div role="img" aria-label="Photo of dancers in rehearsal" style="background:linear-gradient(#6f5a7e,#3e3552)"></div>
      <div role="img" aria-label="Photo of a dance performance on stage" style="background:linear-gradient(#8a6e9a,#4a3a6b)"></div>
    </div>
  </div>
</section>
</body>
</html>
```